Solar energy proposal for homeowners

I am providing households with solar energy proposals, and I need a high-quality brochure that is packaged cleverly to attract the homeowner's attention. Take a look at the one page solar brochure that I have included to get an idea of text and content.

Target Market(s)

Residential Homeowners

Industry/Entity Type

Solar

Requirements
Must have
• High quality document

```html
<!DOCTYPE html>
<html lang="en">
<head>
<meta charset="utf-8">
<title>Brightvale Energy – Solar for $0 Down</title>
<link href="https://fonts.googleapis.com/css2?family=Archivo:wght@500;700;800;900&family=Source+Sans+3:wght@400;500&display=swap" rel="stylesheet">
<style>
  :root{
    --navy:#172460;
    --orange:#f59f0a;
    --green:#8dc63f;
    --teal:#27b8c4;
    --white:#ffffff;
    --mist:#e4e6ee;
    --red:#e0202b;
    --photo-top:#d9b48a;
    --photo-mid:#6f6a5e;
    --photo-low:#4d6b2a;
  }
  *{margin:0;padding:0;box-sizing:border-box}
  html,body{width:848px;height:1200px;overflow:hidden;background:var(--white)}
  .brochure{position:relative;width:848px;height:1200px;overflow:hidden;background:var(--navy);font-family:"Source Sans 3",Arial,sans-serif}
  .hero-shapes{position:absolute;left:0;top:0}
  .brand{position:absolute;left:42px;top:62px;display:flex;align-items:center;gap:16px}
  .brand-mark{width:40px;height:40px;background:var(--teal)}
  .brand-name{font-family:"Archivo",Arial,sans-serif;font-weight:500;font-size:40px;color:var(--teal);letter-spacing:.5px}
  .headline{position:absolute;left:40px;top:200px;font-family:"Archivo",Arial,sans-serif;font-weight:900;color:var(--white);font-size:47px;line-height:50px;letter-spacing:1px}
  .tagline{position:absolute;left:41px;top:410px;font-family:"Archivo",Arial,sans-serif;font-weight:700;color:var(--white);font-size:18px;line-height:22px}
  .tagline span{display:block;font-size:15px;line-height:20px}
  .about{position:absolute;left:0;top:473px;width:424px;height:657px;background:var(--green);padding:44px 26px 0 41px}
  .section-title{font-family:"Archivo",Arial,sans-serif;font-weight:700;color:var(--white);font-size:37px;line-height:40px}
  .about p{margin-top:18px;color:var(--navy);font-size:21.5px;line-height:30.3px}
  .why{margin-top:30px}
  .reasons{list-style:none;margin-top:6px}
  .reasons li{position:relative;padding-left:27px;color:var(--navy);font-size:26px;line-height:37.6px}
  .reasons li::before{content:"";position:absolute;left:1px;top:15px;width:11px;height:11px;border-radius:50%;background:var(--white)}
  .reasons b{font-weight:400;color:var(--red)}
  .services{position:absolute;left:424px;top:473px;width:424px;height:657px;padding:38px 0 0 26px}
  .services .section-title{color:var(--mist);font-size:39px;font-weight:800}
  .service{position:absolute;left:26px;display:flex;gap:19px}
  .service-icon{flex:none;width:80px;height:67px;border-radius:14px;background:var(--green);display:flex;align-items:center;justify-content:center}
  .service h3{font-family:"Archivo",Arial,sans-serif;font-weight:700;color:var(--green);font-size:16px;line-height:18px;margin-top:-6px;margin-bottom:4px}
  .service p{color:var(--white);font-size:15.5px;line-height:17.5px;width:260px}
  .footer{position:absolute;left:0;top:1130px;width:848px;height:70px;background:var(--orange);font-family:"Archivo",Arial,sans-serif;font-weight:700;color:var(--white);font-size:14.5px}
  .contact{position:absolute;top:18px;display:flex;align-items:center;gap:8px}
</style>
</head>
<body>
<main class="brochure">
  <svg class="hero-shapes" width="848" height="476" viewBox="0 0 848 476">
    <defs>
      <linearGradient id="photoTone" x1="0" y1="0" x2="0" y2="1">
        <stop offset="0" stop-color="var(--photo-top)"/>
        <stop offset=".55" stop-color="var(--photo-mid)"/>
        <stop offset="1" stop-color="var(--photo-low)"/>
      </linearGradient>
    </defs>
    <polygon points="444,0 848,0 848,476 464,476 548,329 444,175" fill="url(#photoTone)" role="img" aria-label="Photo of a modern home with solar panels on its roofs at sunset, with a wooden boardwalk and garden"/>
    <polygon points="0,175 415,175 515,329 430,473 0,473" fill="var(--orange)"/>
  </svg>

  <div class="brand">
    <span class="brand-mark"></span>
    <span class="brand-name">Brightvale Energy</span>
  </div>

  <h1 class="headline">SOLAR FOR $0<br>DOWN.<br>NO LIENS.<br>NO KIDDING</h1>
  <p class="tagline">POWER YOUR FUTURE WITH<span>BRIGHTVALE ENERGY</span></p>

  <section class="about">
    <h2 class="section-title">ABOUT US</h2>
    <p>At Brightvale Energy, our mission is to make solar simple and accessible for everyone. No high-pressure sales, just the information you need to make a smart choice. With our solar rental program, you can lower your monthly energy costs and pay less than your current electricity bill.</p>
    <h2 class="section-title why">WHY CHOOSE US?</h2>
    <ul class="reasons">
      <li><b>No</b> financing</li>
      <li><b>No</b> liens</li>
      <li><b>No</b> down payment</li>
      <li><b>No</b> insurance costs</li>
      <li><b>No</b> long-term commitment</li>
      <li><b>No</b> maintenance costs</li>
    </ul>
  </section>

  <section class="services">
    <h2 class="section-title">OUR BEST SERVICE</h2>

    <div class="service" style="top:125px">
      <div class="service-icon">
        <svg width="48" height="48" viewBox="0 0 48 48" fill="none" stroke="var(--navy)" stroke-width="2.6" stroke-linecap="round">
          <path d="M17 28a11 11 0 1 1 14 0v5H17z"/><path d="M18 37h12M19 41h10M24 3v4M8 10l3 3M40 10l-3 3M3 24h4M41 24h4"/><path d="M24 33v-9l-3-3 3-4 3 4-3 3"/>
        </svg>
      </div>
      <div><h3>AFFORDABLE &amp; TRANSPARENT</h3><p>Simple pricing, no hidden fees and a fixed monthly rate lower than typical energy bills.</p></div>
    </div>

    <div class="service" style="top:259px">
      <div class="service-icon">
        <svg width="58" height="54" viewBox="0 0 58 54" fill="none" stroke="var(--navy)" stroke-width="3" stroke-linecap="round">
          <circle cx="25" cy="30" r="21"/><circle cx="25" cy="30" r="14"/><circle cx="25" cy="30" r="7"/><path d="M25 30L50 5M44 4h7v7"/>
        </svg>
      </div>
      <div><h3>LOCAL EXPERTISE</h3><p>Florida-based team that understands the needs of Orlando and statewide homeowners.</p></div>
    </div>

    <div class="service" style="top:393px">
      <div class="service-icon">
        <svg width="58" height="52" viewBox="0 0 58 52" fill="none" stroke="var(--navy)" stroke-width="5" stroke-dasharray="5 4">
          <circle cx="20" cy="20" r="13"/><circle cx="39" cy="34" r="12"/>
          <circle cx="20" cy="20" r="5" stroke-width="3" stroke-dasharray="none"/><circle cx="39" cy="34" r="5" stroke-width="3" stroke-dasharray="none"/>
        </svg>
      </div>
      <div><h3>EXPERT INSTALLATION</h3><p>Certified professionals handle installation, maintenance, and repairs end to end.</p></div>
    </div>

    <div class="service" style="top:520px">
      <div class="service-icon">
        <svg width="62" height="54" viewBox="0 0 62 54" fill="var(--navy)">
          <path d="M30 50C8 52 4 34 6 22c10 4 22 10 24 28z"/><path d="M32 48C30 26 40 10 60 6c2 20-8 38-28 42z"/>
        </svg>
      </div>
      <div><h3>ECO-FRIENDLY</h3><p>Clean, renewable solar energy that helps reduce your carbon footprint.</p></div>
    </div>
  </section>

  <footer class="footer">
    <div class="contact" style="left:68px">
      <svg width="27" height="27" viewBox="0 0 27 27"><rect width="27" height="27" rx="5" fill="var(--white)"/><path d="M8 6l3 0 1 5-2 1c1 3 3 5 6 6l1-2 5 1v3c0 1-1 2-2 2C12 21 6 15 6 8c0-1 1-2 2-2z" fill="var(--orange)"/></svg>
      <span>(555) 014-2290</span>
    </div>
    <div class="contact" style="left:250px">
      <svg width="30" height="26" viewBox="0 0 30 26" fill="none" stroke="var(--white)" stroke-width="2"><rect x="1" y="1" width="28" height="24"/><path d="M1 8h28"/><path d="M5 17h5M12 17h5M19 17h5" stroke-width="3"/></svg>
      <span>123 ANYWHERE ST. ANY CITY</span>
    </div>
    <div class="contact" style="left:531px">
      <svg width="27" height="27" viewBox="0 0 27 27" fill="none" stroke="var(--white)" stroke-width="1.8"><circle cx="13.5" cy="13.5" r="12"/><ellipse cx="13.5" cy="13.5" rx="5.5" ry="12"/><path d="M1.5 13.5h24M3.5 7h20M3.5 20h20"/></svg>
      <span>WWW.BRIGHTVALEENERGY.COM</span>
    </div>
  </footer>
</main>
</body>
</html>
```